Book cover for "Steady Harbor" focused on scaling up an Insurance Agency

Front Cover:
We need book cover for our upcoming book with title "Steady Harbor" . Subtitle of book is "The secrets behind building a multi-million dollar Insurance agency:Interviews, success stories and framework for success".
On top line it should say " Foreword by Mark Vellison".
Author name : "Rajendra Kulkat"
This book will help insurance agents in scaling up their agency. It will also help someone looking to start a business or side hustle.

Back Cover:
It should contain content provided below and image of author attached.
"
Who should read this book?

Do you know that starting an Insurance Agency is probably one of the best business ideas?
Do you want to know how some startups created billion dollar plus insurance based companies in the last 5-10 years?
Do you want to know the secrets behind building a multi-million dollar Insurance agency?
Do you want to know how to scale up an Insurance Agency profitably?
Do you want to know how to cut through the noise in the market and differentiate your business?
How to leverage technology to rise above (be seen and heard) the myriad of agencies around you and compete with both local and online agencies?
How to build a team which carries your mindset to take care of clients and grow your business?
(above list should be bulleted)
If you are interested in learning about these topics then you are at the right place.

You can either spend years figuring out things yourself or read this book and get wisdom from successful agents and thought leaders at top insurance agencies."

Spine:
" Steady Harbor by Rajendra Kulkat"

Requirements:
One file should be only book cover.
Other file should contain :front cover, back cover and spine as one file.
It should follow standard for Brimlow Press, link provided below.
https://print.brimlowpress.example/en_US/help/topic/Q738210465

Target Market(s)

Insurance Agents
People looking to start a new business
Side Hustlers

Industry/Entity Type

Insurance Agency

Font styles to use
Serif

```html
<!DOCTYPE html>
<html lang="en">
<head>
<meta charset="utf-8">
<title>Steady Harbor — Full Cover Wrap</title>
<link rel="stylesheet" href="https://fonts.googleapis.com/css2?family=Cinzel:wght@400;500&family=Sorts+Mill+Goudy&family=Crimson+Pro:wght@600&display=swap">
<style>
  :root {
    --sky-top: #a9e3f7;
    --sky-mid: #d4f0fb;
    --sky-low: #f3fbfe;
    --ink: #0d0d0d;
    --panel-top: #f7f7f9;
    --panel-low: #e8e8ee;
    --suit: #1f2838;
    --skin: #b88a6e;
    --photo-wall: #e9e6df;
    --photo-jacket: #aeb6cc;
  }
  html, body {
    margin: 0;
    padding: 0;
    overflow: hidden;
    background: #ffffff;
  }
  .cover-wrap {
    position: relative;
    width: 1200px;
    height: 854px;
    overflow: hidden;
    background: linear-gradient(180deg, var(--sky-top) 0%, var(--sky-mid) 45%, var(--sky-low) 80%, #ffffff 100%);
    color: var(--ink);
  }
  .decor-curves {
    position: absolute;
    inset: 0;
    pointer-events: none;
  }

  /* Back cover */
  .back-heading {
    position: absolute;
    left: 44px;
    top: 56px;
    margin: 0;
    font: 400 19px/1 "Sorts Mill Goudy", serif;
  }
  .reader-list {
    position: absolute;
    left: 44px;
    top: 91px;
    width: 500px;
    margin: 0;
    padding: 0;
    list-style: none;
    font: 400 18px/21.5px "Sorts Mill Goudy", serif;
  }
  .reader-list li {
    position: relative;
    padding-left: 24px;
    margin-bottom: 6px;
  }
  .reader-list li::before {
    content: "";
    position: absolute;
    left: 2px;
    top: 6px;
    width: 10px;
    height: 10px;
    border-radius: 50%;
    background: var(--ink);
  }
  .author-photo {
    position: absolute;
    left: 58px;
    top: 474px;
    width: 217px;
    height: 289px;
    background: linear-gradient(180deg, var(--photo-wall) 0%, var(--photo-wall) 45%, var(--photo-jacket) 100%);
  }
  .back-blurb {
    position: absolute;
    left: 300px;
    top: 474px;
    width: 232px;
    font: 400 18px/21.5px "Sorts Mill Goudy", serif;
    text-align: justify;
  }
  .back-blurb p { margin: 0 0 21.5px; }

  /* Spine */
  .spine-text {
    position: absolute;
    left: 601px;
    top: 0;
    margin: 0;
    transform-origin: 0 0;
    transform: translateX(19px) rotate(90deg);
    white-space: nowrap;
    font: 400 35px/38px "Cinzel", serif;
  }
  .spine-title { top: 68px; }
  .spine-author { top: 470px; }

  /* Front cover */
  .foreword {
    position: absolute;
    left: 680px;
    width: 460px;
    top: 25px;
    margin: 0;
    text-align: center;
    font: 400 21px/1 "Sorts Mill Goudy", serif;
  }
  .front-title {
    position: absolute;
    left: 670px;
    width: 490px;
    top: 72px;
    margin: 0;
    text-align: center;
    font: 400 92px/82px "Cinzel", serif;
    letter-spacing: 1px;
  }
  .people-left {
    position: absolute;
    left: 657px;
    top: 334px;
    width: 84px;
    height: 383px;
    border-radius: 40px 0 0 40px;
    background: linear-gradient(180deg, var(--skin) 0%, var(--skin) 22%, var(--suit) 32%, var(--suit) 55%, var(--skin) 60%, var(--skin) 78%, #3a2a24 100%);
  }
  .people-right {
    position: absolute;
    left: 1098px;
    top: 360px;
    width: 72px;
    height: 323px;
    border-radius: 0 36px 36px 0;
    background: linear-gradient(180deg, #6e4a3a 0%, var(--skin) 25%, #d9dde6 45%, #d2a88c 65%, var(--suit) 85%, var(--suit) 100%);
  }
  .subtitle-panel {
    position: absolute;
    left: 732px;
    top: 277px;
    width: 372px;
    height: 489px;
    background: linear-gradient(180deg, var(--panel-top) 0%, var(--panel-low) 100%);
    box-shadow: 0 1px 3px rgba(0, 0, 0, 0.08);
  }
  .subtitle {
    position: absolute;
    left: 0;
    right: 0;
    top: 46px;
    margin: 0;
    text-align: center;
    white-space: nowrap;
    font: 600 38px/49px "Crimson Pro", serif;
  }
  .front-author {
    position: absolute;
    left: 660px;
    width: 510px;
    top: 786px;
    margin: 0;
    text-align: center;
    white-space: nowrap;
    font: 400 36px/1 "Cinzel", serif;
    letter-spacing: 3px;
  }
</style>
</head>
<body>
<main class="cover-wrap">
  <svg class="decor-curves" width="1200" height="854" viewBox="0 0 1200 854" aria-hidden="true">
    <path d="M1000 90 Q1150 160 1130 420" fill="none" stroke="#ffffff" stroke-opacity="0.55" stroke-width="14"/>
    <path d="M250 0 Q180 200 260 420" fill="none" stroke="#ffffff" stroke-opacity="0.25" stroke-width="40"/>
  </svg>

  <section class="back-cover">
    <h2 class="back-heading">Who should read this book?</h2>
    <ul class="reader-list">
      <li>Do you know that starting an Insurance Agency is probably one of the best business ideas?</li>
      <li>Do you want to know how some startups created billion dollar plus insurance based companies in the last 5-10 years?</li>
      <li>Do you want to know the secrets behind building a<br>multi-million dollar Insurance agency?</li>
      <li>Do you want to know how to scale up an Insurance Agency profitably?</li>
      <li>Do you want to know how to cut through the noise in the market and differentiate your business?</li>
      <li>How to leverage technology to rise above (be seen and heard) the myriad of agencies around you and compete with both local and online agencies?</li>
      <li>How to build a team which carries your mindset to take care of clients and grow your business?</li>
    </ul>
    <div class="author-photo" role="img" aria-label="Portrait photo of the author in a light grey blazer"></div>
    <div class="back-blurb">
      <p>If you are interested in learning about these topics then you are at the right place.</p>
      <p>You can either spend years figuring out things yourself or read this book and get wisdom from successful agents and thought leaders at top insurance agencies.</p>
    </div>
  </section>

  <section class="spine">
    <p class="spine-text spine-title">STEADY HARBOR</p>
    <p class="spine-text spine-author">RAJENDRA KULKAT</p>
  </section>

  <section class="front-cover">
    <p class="foreword">Foreword by Mark Vellison</p>
    <h1 class="front-title">STEADY<br>HARBOR</h1>
    <div class="people-left" role="img" aria-label="Photo of two smiling business people peeking from behind the panel"></div>
    <div class="people-right" role="img" aria-label="Photo of two smiling business people peeking from behind the panel"></div>
    <div class="subtitle-panel">
      <p class="subtitle">The secrets<br>behind building a<br>multi-million dollar<br>Insurance agency:<br>Interviews,<br>success stories<br>and framework<br>for success.</p>
    </div>
    <p class="front-author">RAJENDRA KULKAT</p>
  </section>
</main>
</body>
</html>
```